Security Guard company needs new procedure template to wow potential clients in tender submissions

We need an update to our procedure template that will look very professional and modern. We have many procedures so this template must be editable so the content can be adjusted by us depending on the procedure.
A smart and modern professional front page with editable title etc.
A professional and modern page template for the body of the procedure.

We wish to copy and paste our word document onto this template and be able to use it easily.

I have attached our logo and example of a procedure we have.

Font styles to use
Sans Serif

Requirements
Must have
• Ability for me to edit text and add new sections to the document.
Use as a template for multiple procedures.

```html
<!DOCTYPE html>
<html lang="en">
<head>
<meta charset="utf-8">
<title>Ridgeline Security Services – Procedure Template</title>
<link href="https://fonts.googleapis.com/css2?family=Open+Sans:wght@400;600;700&display=swap" rel="stylesheet">
<style>
  :root {
    --backdrop: #e9e9ea;
    --page-white: #ffffff;
    --page-tint: #eceaf1;
    --brand-red: #a8202f;
    --brand-red-dark: #7d1622;
    --brand-red-light: #c22a3a;
    --frame-black: #111111;
    --ink: #1c1c1c;
    --rule-grey: #9a9a9a;
    --strip-grey: #d4d4d8;
  }
  * { box-sizing: border-box; margin: 0; padding: 0; }
  html, body { width: 1200px; height: 789px; overflow: hidden; }
  body {
    background: var(--backdrop);
    font-family: "Open Sans", Arial, sans-serif;
    color: var(--ink);
    position: relative;
  }
  .spread {
    position: absolute;
    left: 165px; top: 92px;
    width: 870px; height: 604px;
    display: flex; gap: 10px;
  }
  .page {
    width: 430px; height: 604px;
    position: relative;
    box-shadow: 0 6px 18px rgba(0,0,0,.18);
  }
  /* Procedure body page */
  .procedure-page {
    background: linear-gradient(135deg, var(--page-white) 0%, var(--page-tint) 100%);
    padding: 34px 28px;
  }
  .faint-mark {
    position: absolute; left: 105px; top: 230px;
    width: 220px; height: 220px; border-radius: 50%;
    background: rgba(168,32,47,.06);
  }
  .section-title {
    position: relative;
    background: var(--brand-red);
    color: #fff;
    font-weight: 700; font-size: 15px;
    padding: 5px 10px;
    border-bottom: 6px solid var(--strip-grey);
  }
  .section-intro {
    position: relative;
    font-size: 11px; font-weight: 600; line-height: 1.45;
    margin: 10px 6px 14px;
  }
  .screening-box {
    position: relative;
    border: 1px solid var(--rule-grey);
    margin: 0 6px;
  }
  .screening-box-head {
    background: var(--strip-grey);
    font-size: 10px; font-weight: 600;
    padding: 4px 8px;
  }
  .drug-list { list-style: none; padding: 8px 10px 10px; }
  .drug-list li {
    font-size: 9.5px; line-height: 1.55;
    display: flex; align-items: center; gap: 6px;
  }
  .drug-list svg { width: 9px; height: 9px; flex: none; }
  .section-closing {
    position: relative;
    font-size: 11px; font-weight: 600; line-height: 1.45;
    margin: 14px 6px 0;
  }
  /* Cover page */
  .cover-page {
    background: var(--page-white);
    padding: 10px;
  }
  .cover-frame {
    width: 100%; height: 100%;
    border: 6px solid var(--frame-black);
    background: radial-gradient(ellipse at 45% 40%, var(--brand-red-light) 0%, var(--brand-red) 45%, var(--brand-red-dark) 100%);
    display: flex; flex-direction: column; align-items: center; justify-content: center;
    gap: 18px;
    padding-bottom: 90px;
  }
  .cover-emblem {
    width: 70px; height: 70px; border-radius: 50%;
    background: #fff;
  }
  .cover-name {
    color: #fff; font-weight: 600;
    font-size: 26px; letter-spacing: 3px; text-align: center; line-height: 1.25;
    text-transform: uppercase;
  }
</style>
</head>
<body>
  <main class="spread">
    <article class="page procedure-page">
      <div class="faint-mark"></div>
      <h2 class="section-title">17. Drug and Alcohol Policy</h2>
      <p class="section-intro">RSSL reserves the right to conduct random or routine drug testing on a regular basis. If selected, an employee will be required to go to our nearest preferred Lab and get tested on the day of selection. If they fail their drug test they will face disciplinary action including dismissal.</p>
      <section class="screening-box">
        <div class="screening-box-head">The drugs that may be routinely screened for include any or all the following:</div>
        <ul class="drug-list">
          <li><svg viewBox="0 0 10 10"><polygon points="5,0 6.2,3.6 10,3.6 6.9,5.8 8.1,9.5 5,7.2 1.9,9.5 3.1,5.8 0,3.6 3.8,3.6" fill="#a8202f"/></svg>Alcohol</li>
          <li><svg viewBox="0 0 10 10"><polygon points="5,0 6.2,3.6 10,3.6 6.9,5.8 8.1,9.5 5,7.2 1.9,9.5 3.1,5.8 0,3.6 3.8,3.6" fill="#a8202f"/></svg>Amphetamines (AMP70)</li>
          <li><svg viewBox="0 0 10 10"><polygon points="5,0 6.2,3.6 10,3.6 6.9,5.8 8.1,9.5 5,7.2 1.9,9.5 3.1,5.8 0,3.6 3.8,3.6" fill="#a8202f"/></svg>Cocaine (COC)</li>
          <li><svg viewBox="0 0 10 10"><polygon points="5,0 6.2,3.6 10,3.6 6.9,5.8 8.1,9.5 5,7.2 1.9,9.5 3.1,5.8 0,3.6 3.8,3.6" fill="#a8202f"/></svg>Opiates (OPI)</li>
          <li><svg viewBox="0 0 10 10"><polygon points="5,0 6.2,3.6 10,3.6 6.9,5.8 8.1,9.5 5,7.2 1.9,9.5 3.1,5.8 0,3.6 3.8,3.6" fill="#a8202f"/></svg>Phencyclidine (PCP)</li>
          <li><svg viewBox="0 0 10 10"><polygon points="5,0 6.2,3.6 10,3.6 6.9,5.8 8.1,9.5 5,7.2 1.9,9.5 3.1,5.8 0,3.6 3.8,3.6" fill="#a8202f"/></svg>Barbiturates (BAR)</li>
          <li><svg viewBox="0 0 10 10"><polygon points="5,0 6.2,3.6 10,3.6 6.9,5.8 8.1,9.5 5,7.2 1.9,9.5 3.1,5.8 0,3.6 3.8,3.6" fill="#a8202f"/></svg>Methadone (MTD)</li>
          <li><svg viewBox="0 0 10 10"><polygon points="5,0 6.2,3.6 10,3.6 6.9,5.8 8.1,9.5 5,7.2 1.9,9.5 3.1,5.8 0,3.6 3.8,3.6" fill="#a8202f"/></svg>Methylenedioxymethamphetamine (ecstasy)</li>
          <li><svg viewBox="0 0 10 10"><polygon points="5,0 6.2,3.6 10,3.6 6.9,5.8 8.1,9.5 5,7.2 1.9,9.5 3.1,5.8 0,3.6 3.8,3.6" fill="#a8202f"/></svg>Marijuana/Cannabinoids (THC)</li>
          <li><svg viewBox="0 0 10 10"><polygon points="5,0 6.2,3.6 10,3.6 6.9,5.8 8.1,9.5 5,7.2 1.9,9.5 3.1,5.8 0,3.6 3.8,3.6" fill="#a8202f"/></svg>Benzodiazepines (BZO)</li>
          <li><svg viewBox="0 0 10 10"><polygon points="5,0 6.2,3.6 10,3.6 6.9,5.8 8.1,9.5 5,7.2 1.9,9.5 3.1,5.8 0,3.6 3.8,3.6" fill="#a8202f"/></svg>Methamphetamine (MAMP)</li>
        </ul>
      </section>
      <p class="section-closing">All employees agree to this random testing as part of their employment contract terms and conditions.</p>
    </article>

    <article class="page cover-page">
      <div class="cover-frame">
        <div class="cover-emblem"></div>
        <h1 class="cover-name">Ridgeline<br>Security Services</h1>
      </div>
    </article>
  </main>
</body>
</html>
```